Pest Control Company needs business card!

Hi there, we need a business card designed for our new Pest Control Company. Ideally this card will be simple, yet feel elegant and high end. We want to use the colours Orange, Black and White. Please see our attached logo for the exact colours.

Business card details:

Phone - 0438 517 264
Name - Gus Halloran
Email - Info@trueguardpest.com.au

We would also like to include the following list with dot points:

SERVICES / INSPECTIONS

Termites, Wood Borers, Ants, Cockroaches, Spiders, Fleas, Mice, Rats, Bed Bugs, & More!

```html
<!DOCTYPE html>
<html lang="en">
<head>
<meta charset="utf-8">
<title>TrueGuard Pest Control – Business Card</title>
<link rel="stylesheet" href="https://fonts.googleapis.com/css2?family=Roboto:wght@400;500;700;900&display=swap">
<style>
  :root {
    --bg: #efefef;
    --card-yellow: #fde11b;
    --ink: #1b1b1b;
    --text: #2a2a2a;
    --accent-red: #e0282a;
    --icon-ring: #f3a51d;
    --faint: rgba(120, 100, 20, 0.12);
  }
  * { margin: 0; padding: 0; box-sizing: border-box; }
  html, body { width: 1200px; height: 800px; overflow: hidden; }
  body {
    background: var(--bg);
    font-family: "Roboto", Arial, sans-serif;
    color: var(--text);
    position: relative;
  }
  .card {
    position: absolute;
    width: 570px;
    height: 330px;
    background: var(--card-yellow);
    overflow: hidden;
  }
  .card--contact { left: 476px; top: 32px; }
  .card--services { left: 170px; top: 406px; }

  .brand {
    position: absolute;
    display: flex;
    align-items: center;
    gap: 12px;
  }
  .brand__name {
    font-weight: 900;
    color: var(--ink);
    text-transform: uppercase;
    line-height: 0.95;
    letter-spacing: -0.5px;
  }
  .brand__dot {
    border-radius: 50%;
    background: var(--ink);
    flex: none;
  }
  .card--contact .brand { left: 52px; top: 58px; }
  .card--contact .brand__name { font-size: 28px; }
  .card--contact .brand__dot { width: 44px; height: 44px; }

  .card--services .brand { left: 139px; top: 62px; }
  .card--services .brand__name { font-size: 50px; }
  .card--services .brand__dot { width: 70px; height: 70px; }

  .decor-mascot {
    position: absolute;
    right: -60px;
    top: 60px;
    width: 300px;
    height: 300px;
    border-radius: 50%;
    background: var(--faint);
  }

  .person {
    position: absolute;
    left: 52px;
    top: 172px;
    font-size: 22px;
    font-weight: 500;
    color: var(--ink);
    text-transform: uppercase;
    letter-spacing: 0.3px;
  }
  .contact-list {
    position: absolute;
    left: 52px;
    top: 206px;
    list-style: none;
  }
  .contact-list li {
    display: flex;
    align-items: center;
    gap: 8px;
    height: 25.5px;
    font-size: 17px;
    color: var(--text);
  }
  .contact-icon { width: 19px; height: 19px; flex: none; }

  .services {
    position: absolute;
    left: 0;
    right: 0;
    top: 248px;
    text-align: center;
    font-size: 19px;
    color: var(--ink);
    line-height: 26px;
  }
  .services__item { white-space: nowrap; }
  .services__item::before {
    content: "";
    display: inline-block;
    width: 8px;
    height: 8px;
    border-radius: 50%;
    background: var(--accent-red);
    margin: 0 5px 2px 2px;
  }
</style>
</head>
<body>

  <section class="card card--contact" aria-label="Business card, contact side">
    <div class="decor-mascot" role="img" aria-label="Faint enlarged brand mascot decoration"></div>

    <div class="brand">
      <p class="brand__name">TrueGuard<br>Pest<br>Control</p>
      <span class="brand__dot" aria-hidden="true"></span>
    </div>

    <h1 class="person">Gus Halloran</h1>

    <ul class="contact-list">
      <li>
        <svg class="contact-icon" viewBox="0 0 20 20" aria-hidden="true">
          <circle cx="10" cy="10" r="9" fill="none" stroke="var(--icon-ring)" stroke-width="1.6"/>
          <path d="M7 5.5l1.6 2.3-1 1.1c.6 1.3 1.6 2.3 2.9 2.9l1.1-1 2.3 1.6-.8 1.8c-3.6-.3-6.6-3.3-6.9-6.9z" fill="var(--accent-red)"/>
        </svg>
        <span>0438 517 264</span>
      </li>
      <li>
        <svg class="contact-icon" viewBox="0 0 20 20" aria-hidden="true">
          <circle cx="10" cy="10" r="9" fill="none" stroke="var(--icon-ring)" stroke-width="1.6"/>
          <rect x="5.5" y="6.8" width="9" height="6.4" rx="0.8" fill="var(--accent-red)"/>
          <path d="M5.8 7.2l4.2 3.2 4.2-3.2" fill="none" stroke="var(--card-yellow)" stroke-width="1"/>
        </svg>
        <span>Info@trueguardpest.com.au</span>
      </li>
      <li>
        <svg class="contact-icon" viewBox="0 0 20 20" aria-hidden="true">
          <circle cx="10" cy="10" r="9" fill="none" stroke="var(--icon-ring)" stroke-width="1.6"/>
          <circle cx="10" cy="10" r="4.8" fill="var(--accent-red)"/>
          <path d="M5.2 10h9.6M10 5.2c-1.8 2.6-1.8 7 0 9.6M10 5.2c1.8 2.6 1.8 7 0 9.6" fill="none" stroke="var(--card-yellow)" stroke-width="0.8"/>
        </svg>
        <span>www.trueguardpest.com.au</span>
      </li>
    </ul>
  </section>

  <section class="card card--services" aria-label="Business card, services side">
    <div class="brand">
      <p class="brand__name">TrueGuard<br>Pest<br>Control</p>
      <span class="brand__dot" aria-hidden="true"></span>
    </div>

    <p class="services">
      <span class="services__item">Termites</span>
      <span class="services__item">Wood Borers</span>
      <span class="services__item">Ants</span>
      <span class="services__item">Cockroaches</span><br>
      <span class="services__item">Spiders</span>
      <span class="services__item">Fleas</span>
      <span class="services__item">Mice</span>
      <span class="services__item">Rats</span>
      <span class="services__item">Bed Bugs, &amp; More!</span>
    </p>
  </section>

</body>
</html>
```